Modern SaaS Dashboard Redesign for Building Management Platform

Overview:
Refer to velmora.com.au
We need a complete visual redesign of our property management dashboard to make it sleek, modern, and highly user-friendly. The current interface is functional but outdated. We want a high end SaaS design that feels intuitive, and visually engaging for daily use.

Style Direction:

Retain existing colour palette
Consistent, modern iconography and typography
Responsive design consideration (desktop-first, but adaptable to mobile)

Deliverables:
High-fidelity dashboard design in Figma or Adobe XD
Style guide for colours, typography, and icons
Layered files for developer handoff

Customer Journey Context

This dashboard is the central control panel for a property management SaaS platform (Velmora) used by building managers, strata managers, and executive committee members to manage building data and operations.

Entry Point: User logs in via the secure portal → lands directly on the dashboard.

Primary Goal: Quickly assess building portfolio health, upcoming actions, and key compliance dates.

Secondary Goal: Navigate smoothly to specific building data, reports, or contractor tasks without getting lost in menus.

Typical Flow:

Glance Phase (0–10 seconds) – User scans top stat cards for red/orange alerts or overdue actions.

Action Phase (10–30 seconds) – Clicks into urgent items from “Next Action List” or stat cards.

Work Phase (1–5 minutes) – Navigates to buildings or reports for detail work, filters/searches, and updates records.

2. Who This is For

Building Managers – Daily operational users, need fast visibility of inspections, insurance, defects, and maintenance.

Strata Managers / Property Managers – Portfolio-level oversight across multiple buildings.

Executive Committee Members (Owners Corporations) – View-only or limited-action users needing transparency and governance oversight.

Internal Support/Admin Staff – Back-office users providing data entry, compliance tracking, and troubleshooting.

3. Stakeholders Who Will See This Dashboard

Internal Admin Team – To monitor user activity and portfolio health.

Portfolio Managers – To track multiple properties at once and ensure compliance deadlines aren’t missed.

Building Service Providers – Certain contractors may have limited dashboard visibility for their assigned properties.

Compliance Officers / Auditors – May access the dashboard to verify documentation and timelines.

4. Key Design Considerations Based on Audience

Immediate clarity – Visual hierarchy that prioritises critical actions first.

Minimal learning curve – Clean, intuitive navigation with consistent patterns.

Quick search/filtering – Users may have dozens or hundreds of buildings to manage.

Mobile awareness – Many building managers work in the field, so components should adapt for tablets and smaller screens.

```html
<!DOCTYPE html>
<html lang="en">
<head>
<meta charset="utf-8">
<title>Velmora – Portfolio Dashboard</title>
<link href="https://fonts.googleapis.com/css2?family=Inter:wght@400;500;600;700&display=swap" rel="stylesheet">
<style>
:root{
  --navy:#1b2a4a;
  --primary:#2c5a92;
  --primary-soft:#e8eef7;
  --bg:#f7f8fa;
  --surface:#ffffff;
  --border:#e3e6ea;
  --text:#1f2328;
  --text-2:#4a4f56;
  --muted:#7a7f87;
  --red:#e53935;
  --red-soft:#fdecec;
  --amber:#f5b400;
  --amber-soft:#fff7e3;
  --green:#2e9e4f;
  --green-soft:#e8f6ec;
  --blue-soft:#e9eef6;
  --chip:#f1f3f5;
}
*{box-sizing:border-box;margin:0;padding:0}
html,body{width:1200px;height:927px;overflow:hidden}
body{font-family:"Inter",sans-serif;color:var(--text);background:var(--surface);font-size:12px}
.app{width:1200px;height:927px;display:grid;grid-template-columns:205px 1fr;grid-template-rows:52px 1fr}
.topbar{grid-column:1/3;display:flex;align-items:center;background:var(--surface);border-bottom:1px solid var(--border);box-shadow:0 2px 6px rgba(0,0,0,.04);position:relative;z-index:2}
.brand{width:205px;padding-left:28px;display:flex;align-items:center;gap:8px;font-weight:700;font-size:17px;color:var(--navy)}
.brand-dot{width:14px;height:14px;border-radius:50%;background:var(--navy)}
.search{width:428px;height:32px;margin-left:-70px;border:1px solid var(--border);border-radius:6px;background:var(--bg);display:flex;align-items:center;gap:9px;padding:0 12px;color:var(--text-2);font-size:12px}
.bell{position:relative;margin-left:24px;width:18px;height:18px}
.bell-count{position:absolute;top:-6px;right:-6px;width:14px;height:14px;border-radius:50%;background:var(--red);color:#fff;font-size:8px;display:grid;place-items:center;font-weight:600}
.user{display:flex;align-items:center;gap:8px;margin-left:18px;font-size:14px;color:var(--text-2)}
.avatar{width:31px;height:31px;border-radius:50%;background:var(--primary);color:#fff;display:grid;place-items:center;font-weight:600;font-size:13px}
.sidebar{background:var(--surface);border-right:1px solid var(--border);padding-top:20px}
.nav-item{display:flex;align-items:center;gap:12px;height:36px;padding-left:20px;font-size:13.5px;color:var(--text-2)}
.nav-item svg{width:14px;height:14px;fill:#555b63}
.nav-item.active{background:var(--primary-soft);color:var(--primary);border-left:3px solid var(--primary);padding-left:20px}
.nav-item.active svg{fill:var(--primary)}
.nav-label{font-size:10px;letter-spacing:1.3px;color:var(--muted);padding:20px 0 8px 20px}
.main{background:var(--bg);padding:18px 21px 0;position:relative}
.page-title{font-size:15.5px;font-weight:600;margin-bottom:14px}
.stats{display:grid;grid-template-columns:repeat(4,1fr);gap:14px;margin-bottom:21px}
.stat{background:var(--surface);border-radius:9px;padding:17px 17px 16px;height:129px;box-shadow:0 1px 3px rgba(0,0,0,.03)}
.stat-head{display:flex;justify-content:space-between;align-items:center;font-size:12px;color:var(--muted)}
.stat-icon{width:34px;height:34px;border-radius:6px;display:grid;place-items:center}
.stat-value{font-size:24px;font-weight:600;color:var(--text-2);margin-top:10px}
.stat-trend{font-size:11px;color:var(--text-2);margin-top:6px;padding-left:6px}
.panel{background:var(--surface);border-radius:9px;padding:18px 21px 21px;margin-bottom:21px}
.panel-head{display:flex;justify-content:space-between;align-items:center;margin-bottom:27px}
.panel-title{font-size:15.5px;font-weight:600}
.tabs{display:flex;gap:7px}
.tab{padding:5px 10px;border-radius:5px;background:var(--chip);font-size:12px;color:var(--text-2)}
.tab.on{background:var(--primary);color:#fff}
.action{display:flex;align-items:center;border:1px solid var(--border);border-radius:6px;height:65px;padding:0 14px;margin-bottom:10px}
.action-icon{width:30px;height:30px;border-radius:6px;display:grid;place-items:center;margin-right:14px}
.action-body{flex:1}
.action-title{font-size:13.5px;color:var(--text-2)}
.action-sub{font-size:11.5px;color:var(--muted);margin-top:4px}
.action-meta{text-align:right;font-size:11.5px;color:var(--text-2)}
.pill{display:inline-block;margin-top:4px;font-size:10px;padding:3px 7px;border-radius:4px}
.pill.high{background:var(--red-soft);color:var(--red)}
.pill.med{background:var(--amber-soft);color:var(--amber)}
.pill.low{background:var(--green-soft);color:var(--green)}
.view-switch{display:flex;align-items:center;gap:6px}
.btn{padding:7px 10px;border-radius:4px;font-size:12px;color:var(--text-2);background:var(--chip)}
.btn.on{background:var(--primary);color:#fff}
.btn.outline{background:var(--surface);border:1.5px solid var(--text);color:var(--text);display:flex;align-items:center;gap:4px}
.buildings{display:grid;grid-template-columns:repeat(3,1fr);gap:14px}
.building{border:1px solid var(--border);border-radius:8px;padding:12px 14px 14px}
.b-head{display:flex;justify-content:space-between;align-items:center;padding-bottom:12px;border-bottom:1px solid var(--border);margin-bottom:10px}
.b-name{font-size:13.5px;font-weight:600;color:var(--text-2)}
.tag{font-size:10px;padding:3px 7px;border-radius:4px}
.tag.urgent{background:var(--red-soft);color:var(--red)}
.tag.clear{background:var(--green-soft);color:var(--green)}
.b-metrics,.b-actions{display:grid;grid-template-columns:1fr 1fr;gap:10px}
.metric{background:var(--bg);border-radius:5px;text-align:center;padding:7px 0 6px}
.metric b{display:block;font-size:14.5px;font-weight:600;color:var(--text-2)}
.metric span{font-size:10px;color:var(--muted)}
.b-actions{margin-top:14px}
.b-btn{background:var(--bg);border-radius:5px;height:26px;display:flex;align-items:center;justify-content:center;gap:5px;font-size:11.5px;color:var(--text-2)}
.b-btn svg{width:12px;height:12px;fill:#4a4f56}
.assistant{position:absolute;right:22px;bottom:20px;width:48px;height:48px;border-radius:50%;background:var(--primary);display:grid;place-items:center;box-shadow:0 4px 10px rgba(44,90,146,.35)}
</style>
</head>
<body>
<div class="app">
  <header class="topbar">
    <div class="brand"><span class="brand-dot"></span>Velmora</div>
    <div class="search">
      <svg width="14" height="14" viewBox="0 0 24 24" fill="none" stroke="#555" stroke-width="2"><circle cx="10" cy="10" r="7"/><path d="M15 15l6 6"/></svg>
      Search buildings, reports, or actions...
    </div>
    <div class="bell">
      <svg width="18" height="18" viewBox="0 0 24 24" fill="#888"><path d="M12 3a6 6 0 0 0-6 6v5l-2 3h16l-2-3V9a6 6 0 0 0-6-6zm-2 16a2 2 0 0 0 4 0z"/></svg>
      <span class="bell-count">3</span>
    </div>
    <div class="user"><span class="avatar">SM</span>Sarah Manager</div>
  </header>

  <aside class="sidebar">
    <div class="nav-item active"><svg viewBox="0 0 16 16"><path d="M1 1h14v14H1zM3 3v4h4V3zm6 0v4h4V3zM3 9v4h4V9zm6 0v4h4V9z"/></svg>Dashboard</div>
    <div class="nav-item"><svg viewBox="0 0 16 16"><path d="M3 1h10v15H9v-3H7v3H3zm2 2v2h2V3zm4 0v2h2V3zM5 7v2h2V7zm4 0v2h2V7z"/></svg>Buildings</div>
    <div class="nav-item"><svg viewBox="0 0 16 16"><path d="M1 2l1 1 2-2 1 1-3 3-2-2zm5 0h10v2H6zM1 7l1 1 2-2 1 1-3 3-2-2zm5 0h10v2H6zm-5 5h3v2H1zm5 0h10v2H6z"/></svg>Tasks &amp; Actions</div>
    <div class="nav-item"><svg viewBox="0 0 16 16"><path d="M3 0h7l4 4v12H3zm2 6v1h7V6zm0 3v1h7V9zm0 3v1h7v-1z"/></svg>Reports</div>
    <div class="nav-item"><svg viewBox="0 0 16 16"><path d="M4 0h2v2h4V0h2v2h3v14H1V2h3zM3 6v8h10V6z"/></svg>Calendar</div>
    <div class="nav-item"><svg viewBox="0 0 16 16"><circle cx="5" cy="4" r="2.5"/><circle cx="11" cy="4" r="2.5"/><path d="M0 12c0-3 2-5 5-5s5 2 5 5zm10 0c0-2-1-4-2-5 5-1 8 1 8 5z"/></svg>Contractors</div>
    <div class="nav-label">MANAGEMENT</div>
    <div class="nav-item"><svg viewBox="0 0 16 16"><path d="M3 0h7l4 4v12H3zm2 9l2 2 4-4-1-1-3 3-1-1z"/></svg>Compliance</div>
    <div class="nav-item"><svg viewBox="0 0 16 16"><path d="M2 1l3 3-1 1 7 7 1-1 3 3-1 1-3-3-1 1-7-7-1 1-1-1zm11 0l2 2-9 9-2-2z"/></svg>Maintenance</div>
    <div class="nav-item"><svg viewBox="0 0 16 16"><path d="M3 0h7l4 4v12H3z"/></svg>Documents</div>
    <div class="nav-label">SETTINGS</div>
    <div class="nav-item"><svg viewBox="0 0 16 16"><path d="M7 0h2l.5 2.2 1.5.7 2-1.2 1.4 1.4-1.2 2 .7 1.5L16 7v2l-2.2.5-.7 1.5 1.2 2-1.4 1.4-2-1.2-1.5.7L9 16H7l-.5-2.2-1.5-.7-2 1.2-1.4-1.4 1.2-2-.7-1.5L0 9V7l2.2-.5.7-1.5-1.2-2 1.4-1.4 2 1.2 1.5-.7zm1 5a3 3 0 1 0 0 6 3 3 0 0 0 0-6z"/></svg>Settings</div>
    <div class="nav-item"><svg viewBox="0 0 16 16"><path d="M8 0a8 8 0 1 1 0 16A8 8 0 0 1 8 0zm0 11a1 1 0 1 0 0 2 1 1 0 0 0 0-2zm0-8C6 3 5 4 5 6h2c0-1 .3-1 1-1s1 .4 1 1c0 1-2 1.2-2 3.5h2C9 8 11 8 11 6c0-2-1.3-3-3-3z"/></svg>Help &amp; Support</div>
  </aside>

  <main class="main">
    <h1 class="page-title">Portfolio Overview</h1>
    <section class="stats">
      <div class="stat">
        <div class="stat-head">Overdue Actions<span class="stat-icon" style="background:var(--red-soft)"><svg width="16" height="16" viewBox="0 0 16 16"><circle cx="8" cy="8" r="8" fill="#e53935"/><rect x="7" y="3.5" width="2" height="6" fill="#fff"/><rect x="7" y="10.8" width="2" height="2" fill="#fff"/></svg></span></div>
        <div class="stat-value">12</div>
        <div class="stat-trend">↑2 today</div>
      </div>
      <div class="stat">
        <div class="stat-head">Upcoming Deadlines<span class="stat-icon" style="background:var(--amber-soft)"></span></div>
        <div class="stat-value">8</div>
        <div class="stat-trend">↓1 resolved</div>
      </div>
      <div class="stat">
        <div class="stat-head">Compliance %<span class="stat-icon" style="background:var(--green-soft)"><svg width="14" height="16" viewBox="0 0 14 16"><path d="M0 2h4V0h6v2h4v14H0z" fill="#2e9e4f"/><path d="M3 9l3 3 5-6" stroke="#fff" stroke-width="1.8" fill="none"/></svg></span></div>
        <div class="stat-value">94%</div>
        <div class="stat-trend">↑3% this month</div>
      </div>
      <div class="stat">
        <div class="stat-head">Active Issues<span class="stat-icon" style="background:var(--blue-soft)"><svg width="16" height="16" viewBox="0 0 16 16" fill="#1b2a4a"><path d="M2 1l3 3-1 1 7 7 1-1 3 3-1 1-3-3-1 1-7-7-1 1-1-1zm11 0l2 2-9 9-2-2z"/></svg></span></div>
        <div class="stat-value">24</div>
        <div class="stat-trend">↓4 resolved</div>
      </div>
    </section>

    <section class="panel">
      <div class="panel-head">
        <h2 class="panel-title">Priority Actions</h2>
        <div class="tabs"><span class="tab on">All</span><span class="tab">Overdue</span><span class="tab">Today</span><span class="tab">Upcoming</span></div>
      </div>
      <div class="action">
        <span class="action-icon" style="background:var(--red-soft)"><svg width="14" height="13" viewBox="0 0 14 13"><path d="M7 0l7 13H0z" fill="#e53935"/><rect x="6.2" y="4" width="1.6" height="5" fill="#fff"/><rect x="6.2" y="10" width="1.6" height="1.6" fill="#fff"/></svg></span>
        <div class="action-body"><div class="action-title">Fire Safety Inspection - Tower A</div><div class="action-sub">Certificate expires in 3 days</div></div>
        <div class="action-meta">Due: Aug 22, 2025<br><span class="pill high">High Priority</span></div>
      </div>
      <div class="action">
        <span class="action-icon" style="background:var(--amber-soft)"><svg width="11" height="14" viewBox="0 0 11 14"><path d="M0 0h7l4 4v10H0z" fill="#f5b400"/><path d="M2 7h7M2 9.5h7" stroke="#fff" stroke-width="1"/></svg></span>
        <div class="action-body"><div class="action-title">Approve Contractor Invoice</div><div class="action-sub">Elevator maintenance - Complex B</div></div>
        <div class="action-meta">Due: Aug 25, 2025<br><span class="pill med">Medium Priority</span></div>
      </div>
      <div class="action" style="margin-bottom:0">
        <span class="action-icon" style="background:var(--green-soft)"><svg width="13" height="14" viewBox="0 0 13 14"><path d="M3 0h1.5v2h4V0H10v2h3v12H0V2h3z" fill="#2e9e4f"/><path d="M3.5 8.5l2 2 4-4" stroke="#fff" stroke-width="1.5" fill="none"/></svg></span>
        <div class="action-body"><div class="action-title">Annual General Meeting</div><div class="action-sub">Prepare agenda and documents</div></div>
        <div class="action-meta">Due: Sep 5, 2025<br><span class="pill low">Low Priority</span></div>
      </div>
    </section>

    <section class="panel">
      <div class="panel-head" style="margin-bottom:27px">
        <h2 class="panel-title">Building Portfolio</h2>
        <div class="view-switch"><span class="btn on">Grid View</span><span class="btn">List View</span><span class="btn outline"><svg width="11" height="11" viewBox="0 0 12 12"><path d="M0 0h12L7 6v6L5 10V6z"/></svg>Filters</span></div>
      </div>
      <div class="buildings">
        <article class="building">
          <div class="b-head"><span class="b-name">Tower A</span><span class="tag urgent">3 Urgent</span></div>
          <div class="b-metrics"><div class="metric"><b>92%</b><span>Compliance</span></div><div class="metric"><b>5</b><span>Open Issues</span></div></div>
          <div class="b-actions">
            <span class="b-btn"><svg viewBox="0 0 16 16"><path d="M8 3C4 3 1 8 1 8s3 5 7 5 7-5 7-5-3-5-7-5zm0 2.5a2.5 2.5 0 1 1 0 5 2.5 2.5 0 0 1 0-5z"/></svg>View</span>
            <span class="b-btn"><svg viewBox="0 0 16 16"><path d="M3 0h7l4 4v12H3z"/></svg>Report</span>
          </div>
        </article>
        <article class="building">
          <div class="b-head"><span class="b-name">Complex B</span><span class="tag clear">All Clear</span></div>
          <div class="b-metrics"><div class="metric"><b>100%</b><span>Compliance</span></div><div class="metric"><b>0</b><span>Open Issues</span></div></div>
          <div class="b-actions">
            <span class="b-btn"><svg viewBox="0 0 16 16"><path d="M8 3C4 3 1 8 1 8s3 5 7 5 7-5 7-5-3-5-7-5zm0 2.5a2.5 2.5 0 1 1 0 5 2.5 2.5 0 0 1 0-5z"/></svg>View</span>
            <span class="b-btn"><svg viewBox="0 0 16 16"><path d="M3 0h7l4 4v12H3z"/></svg>Report</span>
          </div>
        </article>
        <article class="building">
          <div class="b-head"><span class="b-name">Garden Apartments</span><span class="tag urgent">1 Urgent</span></div>
          <div class="b-metrics"><div class="metric"><b>89%</b><span>Compliance</span></div><div class="metric"><b>3</b><span>Open Issues</span></div></div>
          <div class="b-actions">
            <span class="b-btn"><svg viewBox="0 0 16 16"><path d="M8 3C4 3 1 8 1 8s3 5 7 5 7-5 7-5-3-5-7-5zm0 2.5a2.5 2.5 0 1 1 0 5 2.5 2.5 0 0 1 0-5z"/></svg>View</span>
            <span class="b-btn"><svg viewBox="0 0 16 16"><path d="M3 0h7l4 4v12H3z"/></svg>Report</span>
          </div>
        </article>
      </div>
    </section>

    <div class="assistant" aria-label="Assistant">
      <svg width="22" height="20" viewBox="0 0 22 20" fill="#fff"><rect x="10" y="0" width="2" height="4"/><rect x="3" y="4" width="16" height="14" rx="3"/><rect x="0" y="9" width="2" height="5"/><rect x="20" y="9" width="2" height="5"/><circle cx="8" cy="10" r="1.8" fill="#2c5a92"/><circle cx="14" cy="10" r="1.8" fill="#2c5a92"/><rect x="7" y="14" width="8" height="1.5" fill="#2c5a92"/></svg>
    </div>
  </main>
</div>
</body>
</html>
```